Alternative Health Practice - Website redesign

With regard to the welcome image, stock photos can't show the faces of other people. And please don't submit a design for a one-page website.
Hello, I am redesigning a website and need some help from a professional.
The old website is here: peter-lindqvist.net (pls note I don't want to reuse the welcome photo from the old site). Much of the written content will remain the same, so note that I also need a page layout/text colour etc that works for text heavy pages: ie www.peter-lindqvist.net/somatic-articles and www.peter-lindqvist.net/client-reviews
My effort at redesigning is underway here: https://pjlindqvist.sitebuildr.net/my-site-7
The original sitebuildr template is this one: https://www.sitebuildr.net/website-template/view/html/2868?originUrl=https%3A%2F%2Fwww.sitebuildr.net%2Fwebsite%2Ftemplates%2Fhtml%2Fhealth-wellness&tpClick=view_button&esi=6305f015-f1b5-4bdd-8dfa-47b7d756bb68
I'm pretty happy with the colour palette. My name Peter Johan Lindqvist is now the "brand" without Rooted Stillness subtitle. Regarding the Welcome section, if you are going to use my photos, it probably needs to be those two that are already there. If you want to put a stock photo there instead, that's fine.
If you want to propose something quite different to my design, I'm happy to receive design files in Photoshop or whatever and then subsequently replicate on Sitebuildr. Up to you.
Target Market(s)
Mostly women, some men ages 28-60.
Coding
Coded - Design and coding required
Number of Pages Required
5+ page
Look and feel
Each slider illustrates characteristics of the customer's brand and the style your logo design should communicate.

```html
<!DOCTYPE html>
<html lang="en">
<head>
<meta charset="utf-8">
<title>Peter Lindqvist — Energy Healing</title>
<link rel="stylesheet" href="https://fonts.googleapis.com/css2?family=Noto+Sans:wght@400;600;700&display=swap">
<style>
:root{
  --ink:#111;
  --header:#262626;
  --card-dark:#141414;
  --page:#fafafa;
  --white:#fff;
  --gold-a:#bb9439;
  --gold-b:#8c6924;
  --gold-text:#9b7325;
  --contact:#2c2c2c;
}
*{box-sizing:border-box;margin:0;padding:0}
html,body{width:1200px;height:2858px;overflow:hidden}
body{position:relative;background:var(--page);font-family:"Noto Sans",sans-serif;color:var(--ink)}
.abs{position:absolute}
.btn{position:absolute;display:flex;align-items:center;justify-content:center;background:linear-gradient(90deg,var(--gold-a),var(--gold-b));color:var(--white);font-weight:700;font-size:17px;letter-spacing:.3px;border-radius:3px;width:184px;height:49px}
.site-header{left:0;top:0;width:1200px;height:113px;background:var(--header)}
.brand{left:75px;top:16px;width:175px;text-align:center;color:var(--white)}
.brand-mark{width:44px;height:44px;border-radius:50%;background:var(--gold-a);margin:0 auto 6px}
.brand-name{font-size:17px;font-weight:600;letter-spacing:1.6px}
.nav{top:49px;color:var(--white);font-size:17px}
.flag{left:1097px;top:52px;width:28px;height:17px}
.hero{left:0;top:113px;width:1200px;height:747px;background:linear-gradient(135deg,#6d6a5e 0%,#5a574e 35%,#3f3c3a 60%,#2e2b34 100%)}
.hero-shade{left:0;top:113px;width:1200px;height:747px;background:rgba(20,20,20,.25)}
.hero-title{left:0;top:383px;width:1200px;text-align:center;color:var(--white);font-size:58px;font-weight:700;letter-spacing:1px}
.hero-sub{left:0;top:464px;width:1200px;text-align:center;color:var(--white);font-size:20px}
.center{left:0;width:1200px;text-align:center}
.h2{font-size:33px;font-weight:700;letter-spacing:.5px}
.body{font-size:16.5px;line-height:19px}
.about{left:136px;top:1191px;width:943px;height:380px;background:var(--card-dark);border-radius:10px;overflow:hidden}
.about-photo{right:0;top:0;width:330px;height:380px;background:radial-gradient(ellipse at 55% 45%,#6b5140 0%,#3b3028 45%,#141414 80%)}
.review{top:1745px;width:254px;height:285px;background:var(--white);border-radius:8px;box-shadow:0 2px 14px rgba(0,0,0,.07)}
.review p{position:absolute;left:21px;top:34px;width:215px;font-size:13px;line-height:15.5px}
.avatar{position:absolute;left:20px;top:168px;width:81px;height:81px;border-radius:50%;background:linear-gradient(135deg,#6b4a32,#b58f74)}
.reviewer{position:absolute;left:115px;top:193px;color:var(--gold-text);font-size:13.5px;font-weight:700;line-height:16px}
.contact{left:0;top:2195px;width:1200px;height:663px;background:linear-gradient(160deg,#3a3a3a 0%,var(--contact) 50%,#222 100%)}
.contact-line{left:203px;color:var(--white);font-size:16.5px;line-height:19px}
.form{left:599px;top:2278px;width:488px;height:497px;border:2px solid var(--white);border-radius:14px}
.label{color:var(--white);font-size:15.5px;font-weight:700}
.rule{height:1.5px;background:var(--white)}
.social{top:2574px;width:33px;height:33px;border:2.5px solid var(--white);border-radius:50%}
</style>
</head>
<body>

<header class="site-header abs">
  <div class="brand abs">
    <div class="brand-mark"></div>
    <div class="brand-name">PETER LINDQVIST</div>
  </div>
  <span class="nav abs" style="left:507px">THE PRACTICE</span>
  <span class="nav abs" style="left:650px">ABOUT ME</span>
  <span class="nav abs" style="left:766px">FEEDBACK</span>
  <span class="nav abs" style="left:878px">APPROACH</span>
  <span class="nav abs" style="left:996px">CONTACT</span>
  <svg class="flag abs" viewBox="0 0 28 17" aria-label="Spanish language">
    <rect width="28" height="17" fill="#c60b1e"/><rect y="4.25" width="28" height="8.5" fill="#ffc400"/>
  </svg>
</header>

<div class="hero abs" role="img" aria-label="Photo of a practitioner's hands resting on a client's leg during an energy healing session"></div>
<div class="hero-shade abs"></div>
<h1 class="hero-title abs">ENERGY HEALING</h1>
<p class="hero-sub abs">Balance, Purpose, Success, Creativity, Clarity, Ease, Discovery, Presence, Harmony, Joy</p>
<a class="btn" style="left:508px;top:507px;font-size:16.5px">BOOK A SESSION</a>

<section>
  <h2 class="h2 abs center" style="top:943px">ENERGY HEALING</h2>
  <p class="body abs center" style="top:991px;padding:0 150px">An session begins by identifying your intention or wish.&nbsp; You may be facing physical or emotional challenges or seeking healing with another aspect of your life...</p>
  <a class="btn" style="left:515px;top:1057px">READ MORE</a>
</section>

<section class="about abs">
  <div class="about-photo abs" role="img" aria-label="Portrait photo of Peter Lindqvist"></div>
  <h2 class="h2 abs" style="left:80px;top:94px;color:var(--white)">ABOUT ME</h2>
  <p class="body abs" style="left:80px;top:141px;width:390px;color:var(--white)">Growing up in Scotland I always had a strong connection with nature and the outdoors. Playing outside with friends, with bikes...</p>
  <a class="btn" style="left:80px;top:227px">READ MORE</a>
</section>

<section>
  <h2 class="h2 abs center" style="top:1641px">EXPERIENCE</h2>
  <p class="body abs center" style="top:1689px">Below is feedback sent direct to me from people who have come to the practice.</p>
  <article class="review abs" style="left:198px">
    <p>You have given me a lot of confidence in myself. You are showing me a new way of life. And I've learned that it is possible to handle the physical pain caused by our emotions. I didn't know how to cope with it.&nbsp; Thank you...</p>
    <div class="avatar" role="img" aria-label="Client photo"></div>
    <div class="reviewer">Marta Oliveira<br>Ruiz</div>
  </article>
  <article class="review abs" style="left:481px">
    <p>You have given me a lot of confidence in myself. You are showing me a new way of life. And I've learned that it is possible to handle the physical pain caused by our emotions. I didn't know how to cope with it.&nbsp; Thank you...</p>
    <div class="avatar" role="img" aria-label="Client photo"></div>
    <div class="reviewer">Marta Oliveira<br>Ruiz</div>
  </article>
  <article class="review abs" style="left:763px">
    <p>You have given me a lot of confidence in myself. You are showing me a new way of life. And I've learned that it is possible to handle the physical pain caused by our emotions. I didn't know how to cope with it.&nbsp; Thank you...</p>
    <div class="avatar" role="img" aria-label="Client photo"></div>
    <div class="reviewer">Marta Oliveira<br>Ruiz</div>
  </article>
  <a class="btn" style="left:514px;top:2064px">READ MORE</a>
</section>

<section class="contact abs" role="img" aria-label="Dim background photo of a healing session"></section>
<h2 class="h2 abs" style="left:173px;top:2333px;color:var(--white)">CONTACT US</h2>
<svg class="abs" style="left:173px;top:2404px" width="20" height="26" viewBox="0 0 20 26" fill="none" stroke="#fff" stroke-width="1.6"><path d="M10 25s8-8.5 8-15A8 8 0 0 0 2 10c0 6.5 8 15 8 15z"/><circle cx="10" cy="10" r="3"/></svg>
<p class="contact-line abs" style="top:2404px">Rua das Laranjeiras 12b<br>Bairro do Vale<br>Lisbon, Portugal, 1350-219.</p>
<svg class="abs" style="left:171px;top:2480px" width="24" height="24" viewBox="0 0 24 24" fill="none" stroke="#fff" stroke-width="1.5"><path d="M5 2l4 5-2 3c1.5 3 4 5.5 7 7l3-2 5 4-3 3C11 22 2 13 2 5z"/></svg>
<p class="contact-line abs" style="top:2482px">Telephone/Whatsapp: (+351) 91 000 4827</p>
<svg class="abs" style="left:171px;top:2522px" width="24" height="17" viewBox="0 0 24 17" fill="none" stroke="#fff" stroke-width="1.5"><rect x="1" y="1" width="22" height="15"/><path d="M1 1l11 9 11-9"/></svg>
<p class="contact-line abs" style="top:2519px">Email: info@peter-lindqvist.net</p>
<div class="social abs" style="left:172px" aria-label="Gallery"></div>
<div class="social abs" style="left:218px" aria-label="Journal"></div>

<form class="form abs">
  <span class="label abs" style="left:34px;top:60px">NAME</span>
  <div class="rule abs" style="left:31px;top:97px;width:422px"></div>
  <span class="label abs" style="left:34px;top:134px">EMAIL</span>
  <div class="rule abs" style="left:31px;top:171px;width:195px"></div>
  <span class="label abs" style="left:259px;top:134px">PHONE</span>
  <div class="rule abs" style="left:256px;top:171px;width:195px"></div>
  <span class="label abs" style="left:34px;top:211px">MESSAGE</span>
  <div class="rule abs" style="left:31px;top:324px;width:422px"></div>
  <a class="btn" style="left:31px;top:369px">SUBMIT</a>
</form>

</body>
</html>
```